Cleaning Company and Stayloft Tasks

Our London based company provides services for all things related to Stayloft. Our main tasks are cleaning, checkins & linen. We are in need of a fresh new design that allows customers to book our services with ease.

The site must keep in mind that it will be primarily used on mobile and payment to be taken online.

What we require:

- Two pages designed, Home page (see Homepage doc) and Purchase Page (see flow chart)

Things we like:-

- We like mainly white and pastel based colours.
- Usage of vector style graphics through our the site to represent people & tasks.
- Shopping cart, with lots of images to select services
- Shopping cart that always has the pricing floating on the right
- Shopping cart that is wizard based.
- We like the usage of wonk characters on this site (for us probably angels)
http://www.tradelarks.com/pricing.php
- Slightly quirky design.

Sites we like:
http://vantorigrove.com/ - bold action
https://www.kellimo.com/ - a very playful design

TO AVOID WASTING TIME, INITIALLY DESIGN THE FRONT PAGE ONLY, IF WE LIKE YOUR HOME PAGE DESIGN THEM WE CAN SHORT LIST YOU INTO DESIGNING THE PAYMENT WIZARD PAGE

Target Market(s)

Young working professionals.

Industry/Entity Type

Cleaning Service

Contact Information for Business Card

Name: Rob Parkin
Title: Senior Sales Representative
Tel: +44 (0) 700 9000 0481
Office: +44 (0) 200 946 0718
email: mh@tidyhaven.co.uk
web: www.tidyhaven.co.uk

Number of Pages Required

2 page

Font styles to use
Sans Serif

Colors
876aae
6b449b

Requirements
Must have
• - Two pages designed including home page and wizard to purchase services.
• - Usage of vector images.
Nice to have
• Angels to represent tasks
• We also like the colour yellow, the branding can be changed to suit this colour change.
Should not have
• A design that must not look like a Pagecraft standard Pagecraft theme.

```html
<!DOCTYPE html>
<html lang="en">
<head>
<meta charset="utf-8">
<title>Tidyhaven – Book a Local Professional Cleaner</title>
<link href="https://fonts.googleapis.com/css2?family=Montserrat:wght@400;600;700&family=Open+Sans:wght@400;600&display=swap" rel="stylesheet">
<style>
:root{
  --plum:#5b1f4e;
  --purple:#6b449b;
  --purple-soft:#876aae;
  --ink:#222;
  --grey:#555;
  --dark-circle:#4d4d4d;
  --white:#fff;
  --wood:#5d5852;
  --testi:#2a2624;
}
*{box-sizing:border-box;margin:0;padding:0}
html,body{width:1200px;height:2628px;overflow:hidden;background:var(--white)}
body{position:relative;font-family:"Open Sans",Arial,sans-serif;color:var(--ink)}
.abs{position:absolute}
.head-font{font-family:"Montserrat",Arial,sans-serif}

/* header */
.site-header{left:0;top:0;width:1200px;height:82px;background:var(--plum)}
.brand{left:100px;top:20px;display:flex;align-items:center;gap:10px;color:var(--white);font-family:"Montserrat",sans-serif;font-size:30px;font-weight:400}
.brand-dot{width:30px;height:30px;border-radius:50%;border:2px solid var(--white)}
.main-nav{top:29px;font-family:"Montserrat",sans-serif;font-size:16px;font-weight:600;color:var(--white)}
.nav-sep{top:27px;color:var(--white);font-size:18px}
.login-btn{left:1013px;top:22px;width:88px;height:40px;border:2px solid var(--white);border-radius:4px;color:var(--white);font-family:"Montserrat",sans-serif;font-weight:600;font-size:16px;display:flex;align-items:center;justify-content:center}

/* hero */
.hero-photo{left:0;top:82px;width:1200px;height:517px;background:linear-gradient(100deg,#8c8f8c 0%,#c9c7c2 35%,#ece7df 60%,#d9d4cc 100%)}
.hero-title{left:98px;top:168px;font-family:"Montserrat",sans-serif;font-weight:600;font-size:50px;line-height:62px;color:var(--white)}
.hero-btn{left:100px;top:333px;width:177px;height:54px;border:2px solid var(--white);color:var(--white);font-family:"Montserrat",sans-serif;font-size:17px;display:flex;align-items:center;justify-content:center}
.hero-dots{left:100px;top:440px;display:flex;gap:5px}
.hero-dots span{width:15px;height:15px;border-radius:50%;border:2px solid var(--white)}
.hero-dots span.active{background:var(--purple)}

/* sections */
.section-title{width:1200px;left:0;text-align:center;font-family:"Montserrat",sans-serif;font-weight:700;font-size:27px;color:var(--purple)}
.title-rule{left:550px;width:100px;height:3px;background:var(--purple)}
.intro{left:270px;top:698px;width:660px;text-align:center;font-size:14px;line-height:26px;color:var(--grey)}

.service{top:780px;width:250px;text-align:center}
.service svg{display:block;margin:0 auto;width:100px;height:88px}
.service h3{margin-top:28px;font-family:"Montserrat",sans-serif;font-weight:600;font-size:16px;color:var(--ink)}
.service p{margin:14px auto 0;width:236px;font-size:11px;line-height:19px;color:var(--grey)}
.read-more{display:inline-block;margin-top:16px;width:91px;height:35px;line-height:35px;background:var(--purple);color:var(--white);font-size:12px}

/* why us */
.why-photo{left:0;top:1095px;width:1200px;height:426px;background:linear-gradient(90deg,#4a4540 0%,#6b655e 50%,#7a736b 100%)}
.why-items{left:850px;top:1095px;width:350px;height:426px;background:linear-gradient(160deg,#b77ba0 0%,#8f8a84 40%,#3f6fa8 65%,#d9741e 90%)}
.why{left:100px;top:1122px;color:var(--white);font-family:"Montserrat",sans-serif}
.why h2{font-size:27px;font-weight:700;margin-bottom:18px}
.why h4{font-size:18px;font-weight:600;margin:14px 0 12px}
.why p{font-family:"Open Sans",sans-serif;font-size:14px;line-height:24px;padding-left:25px;position:relative;width:640px}
.why p::before{content:"";position:absolute;left:0;top:6px;width:13px;height:13px;border-radius:50%;background:var(--white)}

/* how it works */
.step{top:1700px;width:140px;height:140px;border-radius:50%;border:5px solid #e6e6e6}
.step.purple{background:var(--purple)}
.step.dark{background:var(--dark-circle)}
.step svg{position:absolute;left:35px;top:35px;width:60px;height:60px}
.badge{width:62px;height:62px;border-radius:50%;border:4px solid var(--white);color:var(--white);font-family:"Montserrat",sans-serif;font-weight:600;font-size:24px;display:flex;align-items:center;justify-content:center}
.badge.purple{background:var(--purple)}
.badge.dark{background:var(--dark-circle)}
.step-label{top:1872px;width:260px;text-align:center;font-size:16px;line-height:25px;color:var(--ink)}
.flow-arrow{width:80px;height:40px}

/* testimonials */
.testi{left:0;top:2003px;width:1200px;height:289px;background:linear-gradient(90deg,#1e1c1b 0%,#3a3532 55%,#2b2725 100%)}
.testi-title{left:0;top:2046px;width:1200px;text-align:center;color:var(--white);font-family:"Montserrat",sans-serif;font-weight:700;font-size:27px}
.testi-quote{left:330px;top:2160px;width:540px;text-align:center;color:var(--white);font-family:"Montserrat",sans-serif;font-weight:600;font-size:17px;line-height:38px}
.quote-mark{color:var(--white);font-family:"Montserrat",sans-serif;font-weight:700;font-size:60px;line-height:1}

/* contact */
.contact-row{left:0;top:2412px;width:1200px;display:flex;justify-content:center;gap:24px;font-size:20px;color:var(--ink)}
.contact-item{display:flex;align-items:center;gap:6px}
.contact-item svg{width:38px;height:38px}
.footer-nav{left:0;top:2490px;width:1200px;display:flex;justify-content:center;gap:24px;font-family:"Montserrat",sans-serif;font-size:16px;color:var(--ink)}
.footer-rule{left:104px;top:2548px;width:1002px;height:2px;background:var(--ink)}
.copyright{left:104px;top:2574px;font-size:14px;color:var(--ink)}
.socials{left:876px;top:2564px;display:flex;gap:12px}
.socials span{width:37px;height:37px;border-radius:50%;border:2px solid var(--ink)}
</style>
</head>
<body>

<header class="site-header abs"></header>
<div class="brand abs"><span class="brand-dot"></span>tidyhaven</div>
<nav>
  <span class="main-nav abs" style="left:582px">HOME</span>
  <span class="nav-sep abs" style="left:664px">|</span>
  <span class="main-nav abs" style="left:704px">ABOUT US</span>
  <span class="nav-sep abs" style="left:818px">|</span>
  <span class="main-nav abs" style="left:857px">CONTACT US</span>
</nav>
<div class="login-btn abs">LOGIN</div>

<div class="hero-photo abs" role="img" aria-label="Smiling cleaner in green apron and yellow gloves wiping a kitchen counter, colleagues cleaning in the background"></div>
<h1 class="hero-title abs">Book a Local<br>Professional Cleaner</h1>
<div class="hero-btn abs">BOOK A SERVICE</div>
<div class="hero-dots abs"><span class="active"></span><span></span><span></span><span></span><span></span></div>

<h2 class="section-title abs" style="top:652px">WHAT WE DO</h2>
<p class="intro abs">Our London based company provides services for all things related to Stayloft. Our main tasks are cleaning,checkins &amp; linen.</p>

<div class="service abs" style="left:71px">
  <svg viewBox="0 0 100 88"><path fill="#6b449b" d="M50 4 4 44h12v40h68V44h12z"/><g fill="#fff"><rect x="40" y="42" width="9" height="9"/><rect x="52" y="42" width="9" height="9"/><rect x="40" y="54" width="9" height="9"/><rect x="52" y="54" width="9" height="9"/></g></svg>
  <h3>Stayloft Tasks</h3>
  <p>Our London based company provides services for all things related to Stayloft. Our main tasks are cleaning,checkins &amp; linen</p>
  <span class="read-more">Read More</span>
</div>
<div class="service abs" style="left:336px">
  <svg viewBox="0 0 100 88"><g fill="#6b449b"><circle cx="40" cy="62" r="22"/><path d="M30 40c-4-20 10-34 26-30l2 6c-12-2-22 8-20 22z"/><rect x="56" y="20" width="6" height="58"/><rect x="56" y="74" width="30" height="6"/></g><circle cx="40" cy="62" r="8" fill="#fff"/></svg>
  <h3>Stayloft Management</h3>
  <p>Our London based company provides services for all things related to Stayloft. Our main tasks are cleaning,checkins &amp; linen</p>
  <span class="read-more">Read More</span>
</div>
<div class="service abs" style="left:611px">
  <svg viewBox="0 0 100 88"><g fill="#6b449b"><rect x="22" y="4" width="5" height="54"/><path d="M14 58h22l4 24H10z"/><path d="M44 42h44l-5 40H49z"/><circle cx="58" cy="32" r="6"/><circle cx="70" cy="28" r="5"/><circle cx="80" cy="34" r="4"/></g></svg>
  <h3>Domestic Cleaning</h3>
  <p>Our London based company provides services for all things related to Stayloft. Our main tasks are cleaning,checkins &amp; linen</p>
  <span class="read-more">Read More</span>
</div>
<div class="service abs" style="left:881px">
  <svg viewBox="0 0 100 88"><g fill="#6b449b"><circle cx="54" cy="24" r="12"/><path d="M34 84V52c0-10 8-16 20-16s20 6 20 16v32z"/><rect x="18" y="6" width="5" height="50"/><rect x="12" y="4" width="17" height="8"/></g><rect x="44" y="56" width="20" height="14" fill="#fff"/></svg>
  <h3>Handyman</h3>
  <p>Our London based company provides services for all things related to Stayloft. Our main tasks are cleaning,checkins &amp; linen</p>
  <span class="read-more">Read More</span>
</div>

<div class="why-photo abs" role="img" aria-label="Dark weathered wooden boards background"></div>
<div class="why-items abs" role="img" aria-label="Cleaning supplies on wood: pink rubber gloves, squeegee, blue and orange spray bottles"></div>
<section class="why abs">
  <h2>WHY US</h2>
  <h4>TRUSTED PROFESSIONALS</h4>
  <p>Our own trusted vetted professionals. They are all experienced, friendly, background checked &amp; insured</p>
  <h4>SAME-DAY AVAILABILITY</h4>
  <p>Book online it take a two minutes, and schedule one of our team at your place as early as the same day.</p>
  <h4>OUR GUARANTEE</h4>
  <p>(If you're not satisfied with our work, we'll send an alternative cleaner to re-do it for free)</p>
</section>

<h2 class="section-title abs" style="top:1572px">HOW IT WORKS</h2>
<div class="title-rule abs" style="top:1622px"></div>

<div class="step purple abs" style="left:112px">
  <svg viewBox="0 0 60 60" fill="none" stroke="#fff" stroke-width="3"><path d="M12 10l8 0 4 10-5 4c3 6 7 10 13 13l4-5 10 4v8c-20 2-36-14-34-34z"/><circle cx="40" cy="16" r="6"/><path d="M30 34c0-6 4-9 10-9s10 3 10 9z"/></svg>
</div>
<div class="badge dark abs" style="left:206px;top:1676px">1</div>
<div class="step dark abs" style="left:366px">
  <svg viewBox="0 0 60 60" fill="none" stroke="#fff" stroke-width="3"><circle cx="30" cy="34" r="20"/><path d="M30 34V22M30 34l8 6M24 8h12M30 8v6"/></svg>
</div>
<div class="badge purple abs" style="left:460px;top:1676px">2</div>
<div class="step purple abs" style="left:655px">
  <svg viewBox="0 0 60 60"><path fill="#fff" d="M12 10h10l5 12-6 5c3 7 8 12 15 15l5-6 12 5v10C30 54 8 34 12 10z"/><path d="M34 10a16 16 0 0 1 16 16M34 18a8 8 0 0 1 8 8" fill="none" stroke="#fff" stroke-width="3"/></svg>
</div>
<div class="badge dark abs" style="left:749px;top:1676px">3</div>
<div class="step dark abs" style="left:929px">
  <svg viewBox="0 0 60 60" fill="#fff"><circle cx="22" cy="22" r="9"/><path d="M6 50c0-12 7-18 16-18s16 6 16 18z"/><circle cx="40" cy="20" r="8"/><path d="M40 30c8 0 14 6 14 18H40c0-8-2-13-6-16 2-1 4-2 6-2z"/></svg>
</div>
<div class="badge purple abs" style="left:1023px;top:1676px">4</div>

<svg class="flow-arrow abs" style="left:270px;top:1800px" viewBox="0 0 80 40" fill="none" stroke="#6b449b" stroke-width="2.5"><path d="M4 20c20 14 50 14 70-6M64 12l10 2-4 10"/></svg>
<svg class="flow-arrow abs" style="left:552px;top:1700px" viewBox="0 0 80 40" fill="none" stroke="#6b449b" stroke-width="2.5"><path d="M4 26c20-20 50-20 70 0M64 30l10-4-2-10"/></svg>
<svg class="flow-arrow abs" style="left:822px;top:1800px" viewBox="0 0 80 40" fill="none" stroke="#6b449b" stroke-width="2.5"><path d="M4 20c20 14 50 14 70-6M64 12l10 2-4 10"/></svg>

<p class="step-label abs" style="left:52px">Select a service</p>
<p class="step-label abs" style="left:306px">Select A time &amp; date you'd like a our professional to attend</p>
<p class="step-label abs" style="left:595px">Pay securely online</p>
<p class="step-label abs" style="left:869px">Sit back, Relax and wait for one of our professionals</p>

<div class="testi abs" role="img" aria-label="Darkened photo of a cleaner at work in a kitchen"></div>
<h2 class="testi-title abs">TESTIMONIALS</h2>
<span class="quote-mark abs" style="left:262px;top:2146px">&ldquo;</span>
<p class="testi-quote abs">Don't just take our word for it; here is what some of our other customers think.</p>
<span class="quote-mark abs" style="left:906px;top:2200px">&rdquo;</span>

<h2 class="section-title abs" style="top:2325px">CONTACT US</h2>
<div class="title-rule abs" style="top:2372px"></div>
<div class="contact-row abs">
  <span class="contact-item"><svg viewBox="0 0 38 38" fill="none" stroke="#222" stroke-width="2"><circle cx="19" cy="19" r="17"/><rect x="10" y="13" width="18" height="12"/><path d="M10 13l9 7 9-7"/></svg>info@tidyhaven.co.uk</span>
  <span class="contact-item"><svg viewBox="0 0 38 38" fill="none" stroke="#222" stroke-width="2"><circle cx="19" cy="19" r="17"/><path d="M12 11h5l2 5-3 2c2 3 4 5 7 6l2-3 5 2v4c-10 1-19-7-18-16z"/></svg>180 000 4417</span>
</div>
<nav class="footer-nav abs">
  <span>HOME</span><span>|</span><span>ABOUT US</span><span>|</span><span>LOGIN</span><span>|</span><span>BLOG</span><span>|</span><span>CONTACT</span>
</nav>
<div class="footer-rule abs"></div>
<p class="copyright abs">Copyright © 2016 Tidyhaven. All Right Reserved</p>
<div class="socials abs"><span></span><span></span><span></span><span></span><span></span></div>

</body>
</html>
```